Visitenkarten für Goldankauf
Zielgruppe
wir sind fokussiert auf den Goldankauf
Aufgabenstellung
es soll elegant aber auch bisschen auffällig sein. aber nichts verspieltes
es heißt die Brennecks Wertecke
logo habe ich nicht

```html
<!DOCTYPE html>
<html lang="de">
<head>
<meta charset="utf-8">
<title>Brennecks Wertecke – Visitenkarten</title>
<link rel="stylesheet" href="https://fonts.googleapis.com/css2?family=Montserrat:wght@300;400;500&display=swap">
<style>
  :root {
    --bg: #e4e4e4;
    --card: #141414;
    --gold: #e3c07f;
    --text: #f2f2f2;
  }
  html, body {
    margin: 0;
    padding: 0;
    width: 1200px;
    height: 898px;
    overflow: hidden;
    background: var(--bg);
    font-family: "Montserrat", sans-serif;
  }
  .canvas {
    position: relative;
    width: 1200px;
    height: 898px;
  }
  .card {
    position: absolute;
    width: 540px;
    height: 300px;
    background: var(--card);
    overflow: hidden;
  }
  .card--front { left: 90px; top: 120px; }
  .card--back  { left: 570px; top: 470px; }

  .brand {
    position: absolute;
    left: 52px;
    top: 126px;
    display: flex;
    align-items: center;
    gap: 14px;
  }
  .brand__dot {
    width: 42px;
    height: 42px;
    border: 2px solid var(--gold);
    border-radius: 50%;
    box-sizing: border-box;
  }
  .brand__name {
    color: var(--gold);
    font-weight: 300;
    font-size: 24px;
    letter-spacing: 0.5px;
  }

  .ring {
    position: absolute;
    left: -70px;
    top: 80px;
    width: 330px;
    height: 330px;
    border: 16px solid var(--gold);
    border-radius: 50%;
    box-sizing: border-box;
  }
  .contact {
    position: absolute;
    left: 290px;
    top: 70px;
    color: var(--text);
    font-size: 13px;
    font-weight: 400;
    line-height: 1.45;
  }
  .contact__address { margin: 0 0 8px; }
  .contact__list { list-style: none; margin: 0; padding: 0; }
  .contact__item { display: flex; align-items: center; gap: 9px; }
  .contact__icon { width: 12px; height: 12px; flex: none; }
</style>
</head>
<body>
<main class="canvas">
  <section class="card card--front" aria-label="Vorderseite">
    <div class="brand">
      <span class="brand__dot"></span>
      <span class="brand__name">Brennecks Wertecke</span>
    </div>
  </section>

  <section class="card card--back" aria-label="Rückseite">
    <div class="ring"></div>
    <div class="contact">
      <p class="contact__address">Lindenallee 14<br>80469 Munich</p>
      <ul class="contact__list">
        <li class="contact__item">
          <svg class="contact__icon" viewBox="0 0 24 24"><path fill="#e3c07f" d="M6.6 10.8a15.1 15.1 0 0 0 6.6 6.6l2.2-2.2a1 1 0 0 1 1-.25 11.4 11.4 0 0 0 3.6.57 1 1 0 0 1 1 1V20a1 1 0 0 1-1 1A17 17 0 0 1 3 4a1 1 0 0 1 1-1h3.5a1 1 0 0 1 1 1c0 1.25.2 2.45.57 3.57a1 1 0 0 1-.25 1z"/></svg>
          089412376540
        </li>
        <li class="contact__item">
          <svg class="contact__icon" viewBox="0 0 24 24"><rect x="6" y="1" width="12" height="22" rx="2" fill="#e3c07f"/><rect x="8" y="4" width="8" height="13" fill="#141414"/></svg>
          01527738419
        </li>
        <li class="contact__item">
          <svg class="contact__icon" viewBox="0 0 24 24"><rect x="2" y="5" width="20" height="14" fill="#e3c07f"/><path d="M2 5l10 8 10-8" fill="none" stroke="#141414" stroke-width="2"/></svg>
          kontakt@brennecks-wertecke.de
        </li>
        <li class="contact__item">
          <svg class="contact__icon" viewBox="0 0 24 24"><circle cx="12" cy="12" r="10" fill="#e3c07f"/><path d="M2 12h20M12 2c3 3 3 17 0 20M12 2c-3 3-3 17 0 20" fill="none" stroke="#141414" stroke-width="1.5"/></svg>
          www.brennecks-wertecke.de
        </li>
      </ul>
    </div>
  </section>
</main>
</body>
</html>
```